Digital course framework design and style

We need a design for a framework to be used on an online course. The framework will have several layers and needs to have a style which can be followed throughout the course. The attached image is at the top level.

Need to keep to the triangle shape and the colour green and red for the words shown in the illustration. The three inner sections are pillars/pathways which we will expand out (Health, Adventure, Creativity) .
The course is Puddles to Pinecones (the inner section) so we need to show the flow from being frustrated with your kids on devices and not trying to be a successful and they can be, moving them to there kids taking action and frustration reducing. So important the framework has the feeling of progression and movement. The issue for each pillar/paths is the red text and the green being the result.

I want the framework to be simple to understand keeping to line diagram but introducing an icon for each piller/path. Needs to look professional and engaging.

I need to be able to edit the framework, present it elements so be in a format I can hide each Piller and display on a mouse click so layered.

Colours should fit into the brand colours

Core colour: #f07f37
Black secondary: #070707
Green : #0A633B
White: #FFFEFE

Website for brand approach: www.meadowandlantern.com

Target Market(s)

Parents of children spending too long on devices

Font styles to use
Sans Serif

Requirements
Must have
• Clear and easy to see outcomes (green words on the example)
Flow from problem to solution (Puddles to Pinecones)
Style to be extended to further piller designs including icons for Health, Adventure, Creativity
Ability to present 1) the promise Puddles to Pinecones 2) each piller in turn
Brand colours included in brief
Should not have
• Busy complicated slide
Keep to line art not complex images

```html
<!DOCTYPE html>
<html lang="en">
<head>
<meta charset="utf-8">
<title>The Spark Trail</title>
<link href="https://fonts.googleapis.com/css2?family=Archivo+Black&family=Montserrat:wght@600;700;800&family=Roboto:wght@500;700&family=Roboto+Condensed:wght@400;500;700&display=swap" rel="stylesheet">
<style>
  :root {
    --brand-orange: #f07f37;
    --brand-black: #070707;
    --brand-green: #0A633B;
    --brand-white: #FFFEFE;
    --issue-red: #e3131b;
  }
  * { box-sizing: border-box; margin: 0; padding: 0; }
  html, body {
    width: 1200px;
    height: 1000px;
    overflow: hidden;
    background: var(--brand-white);
  }
  .framework {
    position: relative;
    width: 1200px;
    height: 1000px;
    background: var(--brand-white);
  }
  .framework-header {
    position: absolute;
    left: 310px;
    top: 20px;
    width: 580px;
    border: 3px solid var(--brand-black);
  }
  .framework-title {
    display: flex;
    align-items: center;
    gap: 12px;
    height: 72px;
    padding-left: 16px;
    background: var(--brand-black);
    color: var(--brand-orange);
    font-family: "Archivo Black", sans-serif;
    font-weight: 400;
    font-size: 47px;
    letter-spacing: 0.5px;
    text-transform: uppercase;
    white-space: nowrap;
  }
  .framework-title-mark {
    flex: none;
    width: 40px;
    height: 40px;
    border-radius: 50%;
    background: var(--brand-orange);
  }
  .framework-subtitle {
    height: 46px;
    display: flex;
    align-items: center;
    justify-content: center;
    background: var(--brand-white);
    color: var(--brand-orange);
    font-family: "Roboto", sans-serif;
    font-weight: 500;
    font-size: 27.5px;
    white-space: nowrap;
  }
  .framework-diagram {
    position: absolute;
    left: 0;
    top: 0;
    width: 1200px;
    height: 1000px;
  }
  .outcome-text {
    fill: var(--brand-green);
    font-family: "Montserrat", sans-serif;
    font-weight: 700;
    font-size: 28px;
  }
  .outcome-ring { fill: none; stroke: var(--brand-orange); stroke-width: 7; }
  .issue-text {
    fill: var(--issue-red);
    font-family: "Roboto Condensed", sans-serif;
    font-weight: 500;
    font-size: 20.5px;
    letter-spacing: 0.3px;
  }
  .path-band { fill: none; stroke: var(--brand-black); stroke-width: 40; stroke-linejoin: miter; stroke-miterlimit: 10; }
  .path-flow-gap { fill: none; stroke: var(--brand-white); stroke-width: 7; stroke-linejoin: miter; }
  .path-label {
    fill: var(--brand-orange);
    font-family: "Montserrat", sans-serif;
    font-weight: 800;
    font-size: 19px;
    letter-spacing: 0.5px;
  }
  .path-icon-disc { fill: var(--brand-black); stroke: var(--brand-white); stroke-width: 2.5; }
  .path-icon-line { fill: none; stroke: var(--brand-orange); stroke-width: 4; stroke-linecap: round; stroke-linejoin: round; }
  .path-icon-fill { fill: var(--brand-orange); }
  .promise-action { fill: var(--brand-green); font-family: "Montserrat", sans-serif; font-weight: 700; font-size: 21px; }
  .promise-action-note { fill: var(--brand-green); font-family: "Montserrat", sans-serif; font-weight: 600; font-size: 15px; }
  .promise-frustration { fill: var(--issue-red); font-family: "Montserrat", sans-serif; font-weight: 700; font-size: 20px; }
  .promise-frustration-note { fill: var(--issue-red); font-family: "Montserrat", sans-serif; font-weight: 600; font-size: 15px; }
  .brand-signoff {
    position: absolute;
    left: 858px;
    top: 880px;
    display: flex;
    align-items: center;
    gap: 8px;
    font-family: "Montserrat", sans-serif;
    font-weight: 700;
    font-size: 17px;
    line-height: 1.1;
    color: var(--brand-black);
  }
  .brand-signoff-square { width: 14px; height: 14px; background: var(--brand-black); }
</style>
</head>
<body>
<main class="framework">

  <header class="framework-header">
    <h1 class="framework-title"><span class="framework-title-mark"></span>The Spark Trail</h1>
    <p class="framework-subtitle">The 3 Paths To Grow Positivity In Your Kids</p>
  </header>

  <svg class="framework-diagram" viewBox="0 0 1200 1000" xmlns="http://www.w3.org/2000/svg">
    <defs>
      <path id="outcome-path-health" d="M276.6 678.1 A365 365 0 0 1 421.8 229.9"/>
      <path id="outcome-path-creativity" d="M778.2 229.9 A365 365 0 0 1 923.4 678.1"/>
      <path id="outcome-path-adventure" d="M345 800 A394 394 0 0 0 858 805"/>
      <linearGradient id="promise-flow" gradientUnits="userSpaceOnUse" x1="600" y1="600" x2="600" y2="495">
        <stop offset="0" stop-color="#e3131b"/>
        <stop offset="0.5" stop-color="#6b3a23"/>
        <stop offset="1" stop-color="#0A633B"/>
      </linearGradient>
    </defs>

    <!-- Outcome ring -->
    <g class="outcome-ring-layer">
      <path class="outcome-ring" d="M425 222 A379 379 0 0 1 772 216"/>
      <path class="outcome-ring" d="M330 780 A385 385 0 0 1 270 690"/>
      <path class="outcome-ring" d="M930 690 A385 385 0 0 1 870 780"/>
    </g>

    <!-- Health pillar -->
    <g class="pillar pillar-health">
      <text class="outcome-text"><textPath href="#outcome-path-health" textLength="490" lengthAdjust="spacingAndGlyphs">Balanced, Fit, Energetic &amp; Focused</textPath></text>
      <text class="issue-text" transform="translate(428 462) rotate(-65.3)" text-anchor="middle">ANXIOUS, OVERWEIGHT, UNFIT &amp; DISCONNECTED</text>
    </g>

    <!-- Creativity pillar -->
    <g class="pillar pillar-creativity">
      <text class="outcome-text"><textPath href="#outcome-path-creativity" textLength="505" lengthAdjust="spacingAndGlyphs">Bright, Ideas driven, Positive &amp; Motivated</textPath></text>
      <text class="issue-text" transform="translate(764 452) rotate(65.5)" text-anchor="middle">UNIMAGINATIVE, NEGATIVE, SCREEN - FOCUSED &amp; TRAPPED</text>
    </g>

    <!-- Adventure pillar -->
    <g class="pillar pillar-adventure">
      <text class="outcome-text"><textPath href="#outcome-path-adventure" textLength="545" lengthAdjust="spacingAndGlyphs">Curious, Connected, Excited &amp; Leading</textPath></text>
      <text class="issue-text" x="598" y="803" text-anchor="middle">INACTIVE, INSULAR, SOLITARY &amp; TIMID</text>
    </g>

    <!-- Pathway triangle -->
    <g class="pathway">
      <polygon class="path-band" points="598,243 822,728 372,728"/>
      <path class="path-flow-gap" d="M574 356 L555 330 L523 333"/>
      <path class="path-flow-gap" d="M771 683 L803 686 L822 660"/>
      <path class="path-flow-gap" d="M434 700 L418 728 L434 756"/>

      <text class="path-label" transform="translate(440 592) rotate(-65.3)" text-anchor="middle" dominant-baseline="central">HEALTH</text>
      <text class="path-label" transform="translate(668 395) rotate(65.5)" text-anchor="middle" dominant-baseline="central">CREATIVITY</text>
      <text class="path-label" x="703" y="728" text-anchor="middle" dominant-baseline="central">ADVENTURE</text>

      <g class="path-icon path-icon-health">
        <circle class="path-icon-disc" cx="477" cy="495" r="37"/>
        <path class="path-icon-fill" d="M477 521 C455 505 449 495 449 485 C449 475 457 469 465 469 C471 469 475 473 477 477 C479 473 483 469 489 469 C497 469 505 475 505 485 C505 495 499 505 477 521 Z"/>
        <path fill="none" stroke="#070707" stroke-width="3" stroke-linejoin="round" d="M445 495 L463 495 L468 485 L475 507 L482 481 L487 495 L509 495"/>
      </g>

      <g class="path-icon path-icon-creativity">
        <circle class="path-icon-disc" cx="716" cy="497" r="37"/>
        <circle class="path-icon-line" cx="716" cy="497" r="13"/>
        <circle class="path-icon-fill" cx="716" cy="497" r="5"/>
        <path class="path-icon-line" d="M716 476 V470 M716 518 V524 M695 497 H689 M737 497 H743 M701 482 L697 478 M731 512 L735 516 M731 482 L735 478 M701 512 L697 516"/>
      </g>

      <g class="path-icon path-icon-adventure">
        <circle class="path-icon-disc" cx="598" cy="728" r="37"/>
        <path class="path-icon-line" d="M574 744 L591 714 L600 728 L608 718 L623 744 Z"/>
      </g>
    </g>

    <!-- Promise -->
    <g class="promise">
      <text class="promise-action" x="598" y="400" text-anchor="middle">Action</text>
      <text class="promise-action-note" x="598" y="418" text-anchor="middle">(in your kids)</text>
      <circle cx="598" cy="453" r="26" fill="#FFFEFE" stroke="#0A633B" stroke-width="2.5"/>
      <circle cx="598" cy="453" r="16" fill="#0A633B" role="img" aria-label="Raised fist icon"/>

      <line x1="598" y1="600" x2="598" y2="500" stroke="url(#promise-flow)" stroke-width="5"/>
      <path d="M587 503 L598 486 L609 503 Z" fill="#0A633B"/>

      <circle cx="598" cy="630" r="26" fill="#FFFEFE" stroke="#e3131b" stroke-width="2.5"/>
      <circle cx="598" cy="630" r="16" fill="#e3131b" role="img" aria-label="Frustrated parent icon"/>
      <text x="598" y="677" text-anchor="middle"><tspan class="promise-frustration-note">(your) </tspan><tspan class="promise-frustration">Frustration</tspan></text>
    </g>
  </svg>

  <div class="brand-signoff">
    <span class="brand-signoff-square"></span>
    <span>Meadow<br>&amp; Lantern</span>
  </div>

</main>
</body>
</html>
```